Author needs eye catching business card design

I need a design that depicts an item from my book Venthe. This item is a blue stone that houses a dragon soul in it. You can vaguely see the shape of a dragon spiraling around the stone in a shimmering blue-silver hue. I've attached my concept design. I've also attached a bookmark concept design to help inspire. I also have attached a picture of a stone that is the color that the stones in my book are. On the back I would like something nice looking but blank for the most part - a space for me to write on if I want. On the front of the card I would like the following stacked upon each other : Fantasy Author, Clara Dovrek, www.cdovrek.com

Contact Information for Business Card

Font styles to use
Serif
Script

Requirements
Must have
• 1 Dragon wisp swirling around inside the stone. I have attached my concept drawing for inspiration.
• The following text stacked upon each other: Fantasy Author, Clara Dovrek, www.cdovrek.com, c_dovrek@mailbrook.net
• The symbols for Glimboard, Lumora, Kinlyst, and Quillet followed by "@claraedovrek"
Should not have
• The exact picture of the stone picture I have attached. This is for color and size/shape inspiration only and is not my own personal picture.
• No pink please.

```html
<!DOCTYPE html>
<html lang="en">
<head>
<meta charset="utf-8">
<title>Clara Dovrek — Business Card</title>
<link rel="stylesheet" href="https://fonts.googleapis.com/css2?family=Great+Vibes&family=Libre+Baskerville&family=Playfair+Display:wght@400&display=swap">
<style>
  :root {
    --backdrop: #1b1b1f;
    --navy: #1d2160;
    --navy-deep: #141747;
    --lapis: #2f3fa8;
    --lapis-light: #5b6fd6;
    --stone-cyan: #4fb6e8;
    --stone-violet: #5a3fb8;
    --panel: rgba(238, 236, 250, 0.9);
    --ink: #1d2160;
    --white: #f4f4fb;
    --muted: #c9cce8;
  }
  * { margin: 0; padding: 0; box-sizing: border-box; }
  html, body { width: 1200px; height: 800px; overflow: hidden; }
  body {
    background: var(--backdrop);
    display: flex;
    flex-direction: column;
    align-items: center;
    justify-content: center;
    gap: 40px;
  }
  .card {
    width: 560px;
    height: 320px;
    border-radius: 18px;
    position: relative;
    overflow: hidden;
    box-shadow: 0 10px 30px rgba(0,0,0,0.5);
  }

  /* Back: note side */
  .card-back {
    background: linear-gradient(135deg, var(--lapis) 0%, var(--navy-deep) 45%, var(--lapis-light) 100%);
  }
  .card-back .stone-border {
    position: absolute; inset: 0;
    background: radial-gradient(circle at 30% 30%, var(--lapis-light), var(--lapis) 45%, var(--navy-deep) 100%);
  }
  .note-panel {
    position: absolute;
    inset: 18px 22px;
    border-radius: 16px;
    background: linear-gradient(160deg, #eeedf9 0%, #d9d8ef 50%, #e8e7f7 100%);
    opacity: 0.95;
    display: flex;
    align-items: center;
    justify-content: center;
  }
  .note-rule {
    display: flex;
    align-items: center;
    gap: 10px;
    width: 78%;
    margin-top: -20px;
  }
  .note-rule .dots { color: var(--ink); font-size: 12px; letter-spacing: 1px; }
  .note-rule .line { flex: 1; height: 1px; background: var(--ink); }
  .note-label {
    font-family: "Great Vibes", cursive;
    font-size: 30px;
    color: var(--ink);
    line-height: 1;
  }

  /* Front: identity side */
  .card-front { background: var(--navy); }
  .dragon-stone {
    position: absolute;
    left: -30px; top: 120px;
    width: 360px; height: 240px;
    border-radius: 50%;
    background: radial-gradient(ellipse at 60% 40%, #bfe9ff 0%, var(--stone-cyan) 25%, var(--lapis) 55%, var(--stone-violet) 80%, var(--navy-deep) 100%);
    transform: rotate(-14deg);
  }
  .stone-bed {
    position: absolute;
    left: 0; bottom: 0;
    width: 100%; height: 100%;
    background: radial-gradient(ellipse at 20% 90%, rgba(47,63,168,0.55), transparent 60%);
  }
  .identity {
    position: absolute;
    right: 28px; top: 46px;
    width: 270px;
    color: var(--white);
    text-align: center;
  }
  .role {
    font-family: "Libre Baskerville", serif;
    font-size: 11px;
    color: var(--muted);
    letter-spacing: 0.5px;
  }
  .author-name {
    font-family: "Great Vibes", cursive;
    font-size: 46px;
    font-weight: 400;
    line-height: 1.1;
    margin: 2px 0 4px;
  }
  .email {
    font-family: "Libre Baskerville", serif;
    font-size: 11px;
  }
  .website {
    font-family: "Libre Baskerville", serif;
    font-size: 11px;
    letter-spacing: 3px;
    margin-top: 4px;
  }
  .socials {
    list-style: none;
    display: flex;
    justify-content: center;
    gap: 10px;
    margin-top: 16px;
  }
  .socials li {
    display: flex;
    align-items: center;
    gap: 4px;
    font-family: "Libre Baskerville", serif;
    font-size: 9px;
    color: var(--white);
  }
  .socials .mark {
    width: 12px; height: 12px;
    border-radius: 2px;
    background: var(--lapis-light);
  }
  .handle {
    font-family: "Libre Baskerville", serif;
    font-size: 11px;
    margin-top: 10px;
  }
</style>
</head>
<body>
  <section class="card card-back" aria-label="Card back">
    <div class="stone-border" role="img" aria-label="Polished lapis lazuli pebbles forming the card border"></div>
    <div class="note-panel" role="img" aria-label="Pale translucent panel over smooth white and lavender pebbles">
      <div class="note-rule">
        <span class="dots">•••</span>
        <span class="line"></span>
        <span class="note-label">Note</span>
        <span class="line"></span>
        <span class="dots">•••</span>
      </div>
    </div>
  </section>

  <section class="card card-front" aria-label="Card front">
    <div class="stone-bed" role="img" aria-label="Dark lapis stones in the background"></div>
    <div class="dragon-stone" role="img" aria-label="Glowing blue stone with a dragon wisp spiraling inside"></div>
    <div class="identity">
      <p class="role">Fantasy Author</p>
      <h1 class="author-name">Clara Dovrek</h1>
      <p class="email">c_dovrek@mailbrook.net</p>
      <p class="website">www.cdovrek.com</p>
      <ul class="socials">
        <li><span class="mark"></span>Glimboard</li>
        <li><span class="mark"></span>Kinlyst</li>
        <li><span class="mark"></span>Quillet</li>
        <li><span class="mark"></span>Lumora</li>
      </ul>
      <p class="handle">@claraedovrek</p>
    </div>
  </section>
</body>
</html>
```